velmu GmbH needs great looking businesscards to leave an impression

Dear Designers,

Our company velmu GmbH based in switzerland needs to have impressive businesscards. We produce and sell high quality bleaching products for the upper market.
We'd like to have a minimalistic but still meaningful design. You'll fine our company logo attached and some of our packaging designs. Our company slogan is "discover your smile". If you need additional information feel free to contact us.
Kind Regards Dano

Dear Designers, This is a business card design contest! I try to call the support to fix that. Kind Regards Dano

```html
<!DOCTYPE html>
<html lang="de">
<head>
<meta charset="utf-8">
<title>velmu GmbH – Visitenkarte</title>
<link rel="stylesheet" href="https://fonts.googleapis.com/css2?family=Mulish:wght@800&family=Questrial&display=swap">
<style>
  :root {
    --card-black: #000000;
    --paper-white: #ffffff;
    --petal-magenta: #d4479c;
    --petal-orange: #f0613f;
    --text-white: #ffffff;
  }
  * { margin: 0; padding: 0; box-sizing: border-box; }
  html, body {
    width: 1200px;
    height: 667px;
    overflow: hidden;
    background: var(--card-black);
  }
  .business-card {
    position: relative;
    width: 1200px;
    height: 667px;
    background: var(--card-black);
    overflow: hidden;
    font-family: "Questrial", "Century Gothic", sans-serif;
    color: var(--text-white);
  }
  .floral-area {
    position: absolute;
    left: 0;
    top: 0;
    width: 640px;
    height: 667px;
  }
  .contact-block {
    position: absolute;
    right: 34px;
    top: 53px;
    text-align: right;
  }
  .company-name {
    font-family: "Mulish", "Century Gothic", sans-serif;
    font-weight: 800;
    font-size: 45px;
    line-height: 45px;
    margin-bottom: 9px;
  }
  .contact-line {
    font-size: 37px;
    line-height: 51px;
    white-space: nowrap;
  }
  .contact-gap { height: 47px; }
  .brand-band {
    position: absolute;
    left: 398px;
    top: 513px;
    width: 802px;
    height: 122px;
    background: var(--paper-white);
    display: flex;
    align-items: center;
    padding-left: 40px;
  }
  .brand-name {
    font-family: "Questrial", "Century Gothic", sans-serif;
    font-size: 80px;
    line-height: 1;
    color: var(--card-black);
  }
</style>
</head>
<body>
  <div class="business-card">
    <svg class="floral-area" viewBox="0 0 640 667" role="img" aria-label="Dekoratives Blütenmuster in Magenta, Orange und Weiss auf Schwarz">
      <defs>
        <linearGradient id="floralTones" x1="0" y1="0" x2="1" y2="1">
          <stop offset="0" stop-color="#d4479c"/>
          <stop offset="0.5" stop-color="#f0613f"/>
          <stop offset="1" stop-color="#d4479c"/>
        </linearGradient>
        <linearGradient id="floralFade" x1="0" y1="0" x2="1" y2="0">
          <stop offset="0" stop-color="#000" stop-opacity="0"/>
          <stop offset="0.7" stop-color="#000" stop-opacity="0.35"/>
          <stop offset="1" stop-color="#000" stop-opacity="1"/>
        </linearGradient>
      </defs>
      <rect width="640" height="667" fill="url(#floralTones)"/>
      <rect width="640" height="667" fill="url(#floralFade)"/>
    </svg>

    <div class="contact-block">
      <p class="company-name">velmu GmbH</p>
      <p class="contact-line">Mister</p>
      <p class="contact-line">Lukas Ferrand</p>
      <p class="contact-line">Lindenhofweg 14</p>
      <p class="contact-line">8047 Zürich</p>
      <div class="contact-gap"></div>
      <p class="contact-line">Mobil: 0041 79 555 01 23</p>
      <p class="contact-line">Mail: lukas.ferrand@velmu.ch</p>
    </div>

    <div class="brand-band">
      <span class="brand-name">velmu</span>
    </div>
  </div>
</body>
</html>
```